Finance Product Agency Business Card Design

We're an agency that provides products (service contracts, gap insurance, tire and wheel, etc) and support to dealership finance departments. We specialize in training finance producers to maximize their potential and also keep them up to date on the ever changing compliance and legal landscape. I'll attach an image of our logo, excited to see what you all come up with. Would also be interested in discussing our new website design with the winner.

Target Market(s)

auto dealerships

Industry/Entity Type

Business

Contact Information for Business Card

Mark Dolvery
Phone 317.624.5583
Fax 855.472.3308
email Mark.Dolvery@brightlanecoverage.example

Requirements
Must have
• basic contact information
Nice to have
• looking for something professional but modern

```html
<!DOCTYPE html>
<html lang="en">
<head>
<meta charset="utf-8">
<title>Brightlane Coverage – Business Card</title>
<link rel="stylesheet" href="https://fonts.googleapis.com/css2?family=Open+Sans:wght@400;700&display=swap">
<style>
  :root {
    --page: #e9e7e4;
    --card: #ffffff;
    --slate: #3c5a6a;
    --divider: #4a4f54;
    --brand-grey: #7d8890;
    --ink: #1e2226;
    --on-slate: #ffffff;
    --shadow: rgba(0, 0, 0, 0.18);
  }
  * { box-sizing: border-box; margin: 0; padding: 0; }
  html, body {
    width: 1200px;
    height: 1120px;
    overflow: hidden;
    background: var(--page);
    font-family: "Open Sans", Arial, sans-serif;
  }
  .canvas {
    width: 1200px;
    height: 1120px;
    display: flex;
    flex-direction: column;
    align-items: center;
    gap: 60px;
    padding-top: 60px;
  }
  .card {
    width: 840px;
    height: 480px;
    background: var(--card);
    box-shadow: 0 10px 30px var(--shadow);
    position: relative;
    overflow: hidden;
  }

  /* Brand lockup */
  .brand {
    display: flex;
    align-items: center;
    gap: 28px;
  }
  .brand-dot {
    width: 110px;
    height: 110px;
    border-radius: 50%;
    background: var(--brand-grey);
    flex: none;
  }
  .brand-name {
    color: var(--brand-grey);
    font-weight: 700;
    font-size: 58px;
    line-height: 1.05;
    letter-spacing: 1px;
    text-transform: uppercase;
  }

  /* Front */
  .card-front {
    display: flex;
    align-items: center;
    justify-content: center;
  }

  /* Back */
  .card-back { display: flex; }
  .back-main {
    width: 58%;
    position: relative;
    display: flex;
    align-items: center;
    padding-left: 40px;
  }
  .back-main .brand { gap: 18px; }
  .back-main .brand-dot { width: 72px; height: 72px; }
  .back-main .brand-name { font-size: 38px; }
  .email {
    position: absolute;
    left: 40px;
    bottom: 34px;
    display: flex;
    align-items: center;
    gap: 10px;
    font-size: 17px;
    color: var(--ink);
  }
  .divider {
    width: 6px;
    background: var(--divider);
    border-left: 2px solid var(--card);
  }
  .back-panel {
    flex: 1;
    background: var(--slate);
    color: var(--on-slate);
    padding: 80px 40px 0 46px;
  }
  .person-name {
    font-weight: 700;
    font-size: 26px;
    letter-spacing: 0.5px;
    margin-bottom: 50px;
  }
  .contact-list { list-style: none; }
  .contact-list li {
    display: flex;
    align-items: center;
    gap: 12px;
    font-size: 19px;
    margin-bottom: 6px;
  }
  .icon { width: 18px; height: 18px; flex: none; }
</style>
</head>
<body>
<main class="canvas">
  <section class="card card-front" aria-label="Card front">
    <div class="brand">
      <span class="brand-dot"></span>
      <span class="brand-name">Brightlane<br>Coverage</span>
    </div>
  </section>

  <section class="card card-back" aria-label="Card back">
    <div class="back-main">
      <div class="brand">
        <span class="brand-dot"></span>
        <span class="brand-name">Brightlane<br>Coverage</span>
      </div>
      <p class="email">
        <svg class="icon" viewBox="0 0 18 18" aria-hidden="true">
          <rect x="1.5" y="4" width="15" height="10" fill="none" stroke="#1e2226" stroke-width="1.6"/>
          <path d="M1.5 4 L9 10 L16.5 4" fill="none" stroke="#1e2226" stroke-width="1.6"/>
        </svg>
        Mark.Dolvery@brightlanecoverage.example
      </p>
    </div>
    <div class="divider"></div>
    <div class="back-panel">
      <h1 class="person-name">Mark Dolvery</h1>
      <ul class="contact-list">
        <li>
          <svg class="icon" viewBox="0 0 18 18" aria-hidden="true">
            <circle cx="9" cy="9" r="7.5" fill="none" stroke="#fff" stroke-width="1.4"/>
            <path d="M6 5 L8 5 L8.6 7.4 L7.4 8.2 Q8.2 10 9.8 10.8 L10.6 9.6 L13 10.2 L13 12 Q9 12.6 6.6 9.8 Q5.4 7.6 6 5 Z" fill="#fff"/>
          </svg>
          317.624.5583
        </li>
        <li>
          <svg class="icon" viewBox="0 0 18 18" aria-hidden="true">
            <rect x="5" y="2" width="8" height="5" fill="#fff"/>
            <rect x="2" y="7" width="14" height="6" rx="1" fill="#fff"/>
            <rect x="5" y="11" width="8" height="5" fill="#fff" stroke="#3c5a6a" stroke-width="1"/>
          </svg>
          855.472.3308
        </li>
        <li>
          <svg class="icon" viewBox="0 0 18 18" aria-hidden="true">
            <circle cx="9" cy="9" r="7" fill="none" stroke="#fff" stroke-width="1.3"/>
            <ellipse cx="9" cy="9" rx="3" ry="7" fill="none" stroke="#fff" stroke-width="1.1"/>
            <line x1="2" y1="9" x2="16" y2="9" stroke="#fff" stroke-width="1.1"/>
          </svg>
          brightlanecoverage.example
        </li>
      </ul>
    </div>
  </section>
</main>
</body>
</html>
```